Harbourline Advisory Group Wordpress Design

See attached brief. If you have questions beyond this please let me know. Brief document is HA Group Website Design v1. Other documents are files from logo creation and business cards to give you an idea of colours and images. Also see document that shows examples of the types of images I want to display on the website.

Focus of site is for customers and to drive traffic from social media etc. Company is startup consulting business in Customer Experience and Contact Centre. We offer benchmarking, strategy reviews, technology audits. etc

Looking for the site to use the existing Wordpress theme on Nestora or something compatible. Happy to change if there is a good reason for doing so.

Has to be easy to manage ongoing if possible.

Target Market(s)

HAG is a consulting organisation in contact centre and customer experience

Number of Pages Required

4 page

Font styles to use
Serif
Sans Serif

Colors
0255a3
3276b5
33a6d7
0293ce
ffffff
fefdec

Requirements
Must have
• Hosted on Nestora so must be compatible. Preference is to use the theme that is already there (Lumeo) unless there is a reason not to
Nice to have
• see brief

```html
<!DOCTYPE html>
<html lang="en">
<head>
<meta charset="utf-8">
<title>Harbourline Advisory Group</title>
<link rel="stylesheet" href="https://fonts.googleapis.com/css2?family=Oswald:wght@300;400&family=Open+Sans:wght@400;600;700&display=swap">
<style>
:root{
  --navy:#0255a3;
  --mid:#3276b5;
  --sky:#33a6d7;
  --bright:#0293ce;
  --band:#1e9cf0;
  --deep:#0a3a7a;
  --ink:#222;
  --muted:#666;
  --dark:#151515;
  --light:#f2f2f2;
  --white:#ffffff;
}
*{margin:0;padding:0;box-sizing:border-box}
html,body{width:1200px;height:4306px;overflow:hidden}
body{position:relative;background:var(--white);font-family:"Open Sans",Arial,sans-serif;color:var(--ink);font-size:14px}
.abs{position:absolute}
.title{position:absolute;left:0;width:1200px;text-align:center;font-family:"Oswald",Arial Narrow,sans-serif;font-weight:300;text-transform:uppercase;font-size:46px;letter-spacing:1px;line-height:1;color:#1a1a1a}
.subtitle{position:absolute;left:0;width:1200px;text-align:center;font-size:13px;font-weight:600;color:#222}
.on-dark{color:var(--white)}

/* header */
.site-header{position:absolute;left:0;top:0;width:1200px;height:92px;background:var(--white)}
.brand{position:absolute;left:100px;top:24px;display:flex;align-items:center;gap:10px}
.brand-mark{width:36px;height:36px;border-radius:50%;background:var(--navy)}
.brand-name{font-size:16px;font-weight:700;color:var(--navy);line-height:1.1}
.main-nav{position:absolute;right:100px;top:36px;display:flex;align-items:center;gap:26px;font-size:13px;color:#333}
.main-nav .active{border:1px solid var(--sky);color:var(--sky);padding:4px 10px}

/* hero */
.hero{position:absolute;left:0;top:92px;width:1200px;height:611px;background:linear-gradient(180deg,#8d9aa8 0%,#b9c3cc 35%,#6d7884 75%,#3a434d 100%)}
.hero-arrow{position:absolute;top:280px;width:36px;height:36px;border-radius:50%;background:rgba(255,255,255,.25)}
.hero-caption{position:absolute;left:100px;top:516px;width:1000px;height:62px;background:rgba(0,0,0,.6);display:flex;align-items:center;justify-content:center;gap:26px;color:var(--white);font-size:18px}
.btn{display:inline-block;background:var(--navy);color:var(--white);font-size:14px;font-weight:600;padding:8px 30px}

.lead{position:absolute;left:110px;top:842px;width:980px;font-size:12.5px;line-height:1.55;color:#444;text-align:center}
.chart{position:absolute;left:345px;top:960px;width:500px;height:280px;background:linear-gradient(135deg,#e8f3fb,#cfe6f5)}
.rule{position:absolute;left:100px;top:1263px;width:1000px;height:1px;background:#ddd}

/* solution */
.feature{position:absolute;top:1435px;width:340px;text-align:center}
.feature-icon{margin:0 auto;width:110px;height:110px;border:1px solid #ccc;display:flex;align-items:center;justify-content:center}
.feature-icon.filled{background:var(--navy);border-color:var(--navy)}
.feature h3{margin-top:36px;font-size:15px;font-weight:700;color:var(--navy)}
.feature p{margin:14px auto 0;width:240px;font-size:13px;line-height:1.45;color:#444}

.callout{position:absolute;left:0;top:1733px;width:1200px;height:112px;background:var(--band);color:var(--white);font-size:20px;font-weight:600;text-align:center;line-height:1.5;padding-top:24px}

/* works */
.works{position:absolute;left:0;top:1845px;width:1200px;height:681px;background:var(--dark)}
.work{position:absolute;top:178px;width:316px}
.work-media{width:316px;height:244px}
.work h4{margin-top:24px;font-size:14px;font-weight:700;color:var(--bright)}
.work p{margin-top:10px;font-size:12px;color:#999}
.pager{position:absolute;top:545px;width:46px;height:46px;border:1px solid #888;display:flex;align-items:center;justify-content:center}
.dots{position:absolute;left:562px;top:626px;display:flex;gap:8px}
.dots i{width:8px;height:8px;border-radius:50%;border:1px solid #888}
.dots i.on{background:var(--bright);border-color:var(--bright)}

/* blog */
.post{position:absolute;top:2698px;width:474px;height:420px}
.post-media{width:474px;height:252px}
.post-badge{position:absolute;left:60px;top:226px;width:42px;height:42px;background:var(--deep);display:flex;align-items:center;justify-content:center}
.post h4{position:absolute;left:110px;top:232px;font-size:17px;font-weight:700;color:#111;background:var(--white);padding:4px 8px 0 0}
.post h4{top:258px;padding:0}
.post-meta{position:absolute;left:0;top:292px;width:80px;text-align:right;font-size:12px;line-height:1.6;color:#444}
.post-text{position:absolute;left:110px;top:292px;width:360px;font-size:13px;line-height:1.55;color:#555}
.read-on{position:absolute;top:388px;font-size:12px;font-weight:700;padding:6px 18px;border:2px solid var(--navy);color:var(--navy)}
.read-on.solid{background:var(--sky);border-color:var(--sky);color:var(--white)}

/* partners */
.partners{position:absolute;left:0;top:3329px;width:1200px;height:316px;background:var(--light);display:grid;grid-template-columns:repeat(5,1fr);grid-template-rows:1fr 1fr}
.partners div{border-right:1px solid #fff;border-bottom:1px solid #fff;display:flex;align-items:center;justify-content:center}
.partners span{width:100px;height:36px;border-radius:6px;background:#c9c9c9}

.cta{position:absolute;left:0;top:3645px;width:1200px;height:126px;background:var(--deep);text-align:center;color:var(--white);font-size:20px;padding-top:22px}
.cta .btn{margin-top:14px;background:var(--band);padding:8px 56px}

/* contact */
.contact-info{position:absolute;left:178px;top:3962px;font-size:14px;line-height:1.45;color:#333}
.contact-info dt{letter-spacing:3px;font-size:13px;color:#555;margin-top:22px}
.contact-info dt:first-child{margin-top:0}
.contact-form{position:absolute;left:436px;top:3932px;width:574px;height:244px;background:#ececec}
.field{position:absolute;background:var(--white);font-size:11px;color:#888;padding:10px 12px}
.send{position:absolute;left:284px;top:170px;width:260px;height:38px;background:var(--band);color:var(--white);font-size:12px;font-weight:700;text-align:center;line-height:38px}
.note{position:absolute;left:436px;top:4192px;font-size:11px;color:#666}

.site-footer{position:absolute;left:0;top:4242px;width:1200px;height:64px;background:var(--deep);color:var(--white);font-size:12px}
.site-footer .copy{position:absolute;left:100px;top:24px}
.social{position:absolute;right:80px;top:18px;display:flex;gap:10px}
.social i{width:28px;height:28px;border-radius:50%;background:#3f7fd0}
</style>
</head>
<body>

<header class="site-header">
  <div class="brand"><span class="brand-mark"></span><span class="brand-name">Harbourline Advisory Group</span></div>
  <nav class="main-nav">
    <span class="active">HOME</span><span>SERVICES</span><span>PARTNERS</span><span>BLOG</span><span>GET IN TOUCH</span>
    <svg width="16" height="16" viewBox="0 0 16 16"><circle cx="6.5" cy="6.5" r="5" fill="none" stroke="#33a6d7" stroke-width="2"/><line x1="10" y1="10" x2="15" y2="15" stroke="#33a6d7" stroke-width="2"/></svg>
  </nav>
</header>

<section class="hero" role="img" aria-label="Business people talking in front of an office window overlooking a city skyline">
  <span class="hero-arrow" style="left:36px"></span>
  <span class="hero-arrow" style="right:36px"></span>
  <div class="hero-caption">You need pragmatic advice on how to accelerate your contact centre maturity? <span class="btn">Read More</span></div>
</section>

<h2 class="title" style="top:748px">What We Do</h2>
<p class="subtitle" style="top:808px">Duis vitae velit mollis, congue nisi dignissim, pellentesque lorem</p>
<p class="lead">Harbourline Advisory Group (HA Group) is a consulting company focused on Customer Experience and Contact Centre Solutions. We are small (a few people) but we bring teams together for projects that have expertise in what is required We are technology experts, but not technology geeks. We don't care that it's cool technology, we care about the changes it can make to Customer Experience and to your bottom line. We not only know who does what in the market, we know how good they are, how good their last projects were and who their channel is and how good their channel is.</p>

<div class="chart" role="img" aria-label="Chart comparing current and desired contact centre maturity across service areas"></div>
<div class="rule"></div>

<h2 class="title" style="top:1296px">Our Solution</h2>
<p class="subtitle" style="top:1356px">Duis vitae velit mollis, congue nisi dignissim, pellentesque lorem</p>

<div class="feature" style="left:85px">
  <div class="feature-icon"><svg width="44" height="40" viewBox="0 0 44 40"><rect x="2" y="2" width="40" height="26" fill="#0255a3"/><rect x="18" y="28" width="8" height="6" fill="#0255a3"/><rect x="12" y="34" width="20" height="3" fill="#0255a3"/></svg></div>
  <h3>BENCHMARKING</h3>
  <p>Nulla sit amet mi sed metus venenatis commodo vitae vel magna. Aenean auctor, dolor dignissim congue</p>
</div>
<div class="feature" style="left:430px">
  <div class="feature-icon filled"><svg width="30" height="40" viewBox="0 0 30 40"><path d="M15 3a11 11 0 0 0-6 20v6h12v-6a11 11 0 0 0-6-20z" fill="#fff"/><rect x="10" y="32" width="10" height="3" fill="#fff"/></svg></div>
  <h3>STRATEGY REVIEWS</h3>
  <p>Nulla sit amet mi sed metus venenatis commodo vitae vel magna. Aenean auctor, dolor dignissim congue</p>
</div>
<div class="feature" style="left:769px">
  <div class="feature-icon"><svg width="44" height="30" viewBox="0 0 44 30"><polyline points="12,5 3,15 12,25" fill="none" stroke="#111" stroke-width="3"/><polyline points="32,5 41,15 32,25" fill="none" stroke="#111" stroke-width="3"/><line x1="26" y1="3" x2="18" y2="27" stroke="#111" stroke-width="3"/></svg></div>
  <h3>TECHNOLOGY AUDITS</h3>
  <p>Nulla sit amet mi sed metus venenatis commodo vitae vel magna. Aenean auctor, dolor dignissim congue</p>
</div>

<div class="callout">Do you feel like you are paying for a Velocar of contact centre solutions but driving it<br>like an Ambler, but without the economy?</div>

<section class="works">
  <h2 class="title on-dark" style="top:38px">Works</h2>
  <p class="subtitle on-dark" style="top:100px">Duis vitae velit mollis, congue nisi dignissim, pellentesque lorem</p>
  <div class="work" style="left:100px">
    <div class="work-media" role="img" aria-label="Team meeting around a table in a bright office" style="background:linear-gradient(160deg,#dbe6f0,#8aa5c2)"></div>
    <h4>CLEMENTINE DE LA FERONNIERE</h4><p>Lorem ipsum</p>
  </div>
  <div class="work" style="left:442px">
    <div class="work-media" role="img" aria-label="Business handshake over a desk" style="background:linear-gradient(160deg,#c7ccd3,#5a6674)"></div>
    <h4>FARMER'S MARKET KITCHEN</h4><p>Contrary popilia</p>
  </div>
  <div class="work" style="left:784px">
    <div class="work-media" role="img" aria-label="Group silhouetted against a large office window" style="background:linear-gradient(180deg,#eef0f0,#7c8186)"></div>
    <h4>BEAUTIFUL GIRL</h4><p>Poplar sit amit</p>
  </div>
  <div class="pager" style="left:536px"><svg width="12" height="16"><polyline points="10,2 3,8 10,14" fill="none" stroke="#fff" stroke-width="2"/></svg></div>
  <div class="pager" style="left:612px"><svg width="12" height="16"><polyline points="2,2 9,8 2,14" fill="none" stroke="#fff" stroke-width="2"/></svg></div>
  <div class="dots"><i class="on"></i><i></i><i></i><i></i><i></i></div>
</section>

<h2 class="title" style="top:2566px">Latest Blog</h2>
<p class="subtitle" style="top:2624px">Duis vitae velit mollis, congue nisi dignissim, pellentesque lorem</p>

<article class="post" style="left:100px">
  <div class="post-media" role="img" aria-label="Colleagues gathered around a laptop in a meeting" style="background:linear-gradient(160deg,#a79b8c,#4a4440)"></div>
  <span class="post-badge"><svg width="18" height="14"><rect x="1" y="1" width="16" height="12" fill="none" stroke="#fff" stroke-width="2"/><polyline points="3,11 7,6 10,9 15,4" fill="none" stroke="#fff" stroke-width="1.5"/></svg></span>
  <h4>LOREM IPSUM DOLOR STI AMIT</h4>
  <div class="post-meta">21 Feb '14<br>John Doe<br>24 Comments</div>
  <p class="post-text">Duis sed odio sit amet nibh vulputate cursus a sit amet mauris. Morbi accumsan ipsum velit. Nam nec tellus a odio tincidunt auctor a ornare odio. Sed non mauris vitae erat consequat auctor eu in elit.</p>
  <span class="read-on" style="left:110px">READ ON</span>
</article>
<article class="post" style="left:626px">
  <div class="post-media" role="img" aria-label="Business crowd against a blue city skyline" style="background:linear-gradient(180deg,#f2f5fa,#6f8fc4)"></div>
  <span class="post-badge"><svg width="18" height="14"><rect x="1" y="1" width="16" height="12" fill="none" stroke="#fff" stroke-width="2"/><polyline points="3,11 7,6 10,9 15,4" fill="none" stroke="#fff" stroke-width="1.5"/></svg></span>
  <h4>CONTANTRY POP SIT</h4>
  <div class="post-meta">21 Feb '14<br>John Doe<br>24 Comments</div>
  <p class="post-text">Duis sed odio sit amet nibh vulputate cursus a sit amet mauris. Morbi accumsan ipsum velit. Nam nec tellus a odio tincidunt auctor a ornare odio. Sed non mauris vitae erat consequat auctor eu in elit.</p>
  <span class="read-on solid" style="left:110px">READ ON</span>
</article>

<h2 class="title" style="top:3198px">Partners</h2>
<p class="subtitle" style="top:3256px">Duis vitae velit mollis, congue nisi dignissim, pellentesque lorem</p>
<div class="partners">
  <div><span></span></div><div><span></span></div><div><span></span></div><div><span></span></div><div><span></span></div>
  <div><span></span></div><div><span></span></div><div><span></span></div><div><span></span></div><div><span></span></div>
</div>

<div class="cta">you need pragmatic advice on how to accelerate your contact centre maturity?<br><span class="btn">MORE</span></div>

<h2 class="title" style="top:3822px">Get In Touch</h2>
<p class="subtitle" style="top:3882px">Duis vitae velit mollis, congue nisi dignissim, pellentesque lorem</p>

<dl class="contact-info">
  <dt>CALL ME</dt><dd>(415) 555-0182</dd>
  <dt>EMAIL ME</dt><dd>hello@harbourline.example</dd>
  <dt>ADDRESS</dt><dd>42 Quayside Lane<br>Port Alder, CA 90000</dd>
</dl>

<form class="contact-form">
  <div class="field" style="left:32px;top:52px;width:224px;height:38px">NAME</div>
  <div class="field" style="left:32px;top:100px;width:224px;height:38px">EMAIL</div>
  <div class="field" style="left:32px;top:148px;width:224px;height:38px">SUBJECT</div>
  <div class="field" style="left:284px;top:52px;width:260px;height:94px">TEXTS</div>
  <div class="send">SEND NOW</div>
</form>
<p class="note">LOOKING FORWARD TO HEARING FROM YOU!</p>

<footer class="site-footer">
  <span class="copy">Copyrights © 2015 harbourline All rights reserved</span>
  <div class="social"><i style="background:#d84a3a"></i><i></i><i style="background:#3aa0e0"></i><i></i></div>
</footer>

</body>
</html>
```